Business cards — need something that creates “wow” factor

Need a sleek and clean looking business card. Something that is clear and consise. These business cards are for my painting business and hundreds will be placed in the Dallas area between all Halverd Pemberton paint stored. These card really need to stick out! Open to any and all ideas...

Target Market(s)

Residential clientele

Industry/Entity Type

Painting

Contact Information for Business Card

Dorian Vakelby
Owner

382.516.2074

Web: Mesahuepainting.example (still under construction)
Mesahuepainting@mailbox.example

Font styles to use
Sans Serif

Colors

Designer to choose colors to be used in the design.

Requirements
Must have
• My name, number, website, email, Socialpage
• and “100% customer satisfaction guaranteed”
• Socialpage.example/Mesahuepainting/
Nice to have
• Listed services
• Interior/exterior painting
• Drywall repair/texture
• Fence staining/refinishing
• Concrete staining
• Epoxy flooring
• Pressure washing

```html
<!DOCTYPE html>
<html lang="en">
<head>
<meta charset="utf-8">
<title>Mesa Hue Painting — Business Cards</title>
<link rel="stylesheet" href="https://fonts.googleapis.com/css2?family=Montserrat:ital,wght@0,400;0,500;1,400&family=Saira+Condensed:wght@300&family=Libre+Baskerville:wght@700&display=swap">
<style>
  :root {
    --stage: #2f3d45;
    --teal: #2fb3c4;
    --teal-deep: #1f8fa8;
    --violet: #6b6fc0;
    --magenta: #b0508f;
    --pink: #d97fb4;
    --band: #ffc80a;
    --ink-blue: #1d3f9e;
    --white: #ffffff;
    --logo-ink: #1b1b1b;
    --frame: #2aa0b4;
  }
  * { box-sizing: border-box; margin: 0; padding: 0; }
  html, body { width: 1200px; height: 900px; overflow: hidden; }
  body {
    background: var(--stage);
    font-family: "Montserrat", sans-serif;
    position: relative;
  }
  .card {
    position: absolute;
    left: 260px;
    width: 680px;
    height: 388px;
    overflow: hidden;
    box-shadow: 0 10px 28px rgba(0,0,0,.35);
  }
  .card--back { top: 40px; }
  .card--front { top: 470px; }
  .card__wash {
    position: absolute; inset: 0;
    background:
      radial-gradient(ellipse 45% 40% at 8% 40%, rgba(107,111,192,.85), transparent 70%),
      radial-gradient(ellipse 40% 35% at 85% 72%, rgba(217,127,180,.9), transparent 70%),
      radial-gradient(ellipse 55% 45% at 60% 20%, rgba(47,179,196,.9), transparent 70%),
      linear-gradient(180deg, var(--teal) 0%, var(--teal-deep) 38%, var(--violet) 60%, var(--magenta) 80%, var(--pink) 100%);
  }
  .logo-box {
    position: absolute;
    background: var(--white);
    display: flex; flex-direction: column; align-items: center; justify-content: center;
    gap: 8px;
  }
  .logo-box__name {
    font-family: "Montserrat", sans-serif;
    font-weight: 500;
    color: var(--logo-ink);
    letter-spacing: .04em;
  }
  .logo-box__tagline {
    font-size: 8px;
    color: var(--logo-ink);
    letter-spacing: .02em;
  }
  .card--back .logo-box {
    left: 228px; top: 20px; width: 224px; height: 188px;
    border: 4px solid var(--white);
    box-shadow: 0 0 0 8px var(--frame) inset, 0 0 0 12px var(--white) inset;
  }
  .card--back .logo-box__name { font-size: 30px; }
  .card--front .logo-box {
    left: 196px; top: 30px; width: 176px; height: 170px;
    box-shadow: 0 4px 10px rgba(0,0,0,.25);
  }
  .card--front .logo-box__name { font-size: 24px; }
  .band {
    position: absolute; left: 0; right: 0;
    background: var(--band);
    color: var(--ink-blue);
    text-align: center;
  }
  .contact-band {
    top: 226px; height: 74px;
    display: flex; flex-direction: column; justify-content: center;
    font-size: 16px; line-height: 21px; letter-spacing: .02em;
  }
  .owner-name {
    position: absolute; left: 404px; top: 62px;
    font-family: "Saira Condensed", sans-serif;
    font-weight: 300;
    font-size: 44px; line-height: 44px;
    letter-spacing: .06em;
    color: var(--white);
    text-transform: uppercase;
  }
  .services {
    top: 220px; height: 96px;
    display: flex; flex-direction: column; justify-content: center;
    font-style: italic; font-size: 18.5px; line-height: 28px;
  }
  .services span::before { content: "• "; }
  .phone {
    position: absolute; left: 0; right: 0; top: 326px;
    display: flex; justify-content: center; align-items: center; gap: 10px;
    font-family: "Libre Baskerville", serif; font-weight: 700;
    font-size: 26px; line-height: 32px; letter-spacing: .08em;
    color: var(--white);
  }
  .guarantee {
    position: absolute; left: 0; right: 0; top: 362px;
    text-align: center;
    font-size: 12px; line-height: 16px; letter-spacing: .08em;
    text-transform: uppercase;
    color: var(--white);
  }
</style>
</head>
<body>
  <section class="card card--back" aria-label="Card back">
    <div class="card__wash" role="img" aria-label="Soft watercolour wash in teal, violet and pink"></div>
    <div class="logo-box">
      <span class="logo-box__name">MESA HUE</span>
      <span class="logo-box__tagline">Commercial | Residential | Interior | Exterior</span>
    </div>
    <div class="band contact-band">
      <p>www.mesahuepainting.example</p>
      <p>Mesahuepainting@mailbox.example</p>
      <p>Socialpage.example/Mesahuepainting/</p>
    </div>
  </section>

  <section class="card card--front" aria-label="Card front">
    <div class="card__wash" role="img" aria-label="Soft watercolour wash in teal, violet and pink"></div>
    <div class="logo-box">
      <span class="logo-box__name">MESA HUE</span>
      <span class="logo-box__tagline">Commercial | Residential | Interior</span>
    </div>
    <h1 class="owner-name">Dorian<br>Vakelby</h1>
    <div class="band services">
      <p><span>Interior/exterior painting</span> <span>Drywall repair/texture</span></p>
      <p><span>Fence staining/refinishing</span> <span>Concrete staining</span></p>
      <p><span>Epoxy flooring</span> <span>Pressure washing</span></p>
    </div>
    <p class="phone">
      <svg width="26" height="26" viewBox="0 0 26 26" aria-hidden="true">
        <circle cx="13" cy="13" r="13" fill="#ffc80a"/>
        <path d="M9 6.5c.6-.4 1.3-.2 1.6.4l1.3 2.4c.3.6.1 1.2-.4 1.6l-.9.6c.6 1.6 1.9 3 3.5 3.8l.7-.9c.4-.5 1.1-.6 1.6-.3l2.3 1.4c.6.3.7 1.1.3 1.6l-.9 1.1c-.6.7-1.6 1-2.5.7C10.8 17.7 8 14.5 7 10.3c-.2-.9.1-1.9.9-2.5z" fill="#ffffff"/>
      </svg>
      382 516 2074
    </p>
    <p class="guarantee">100% customer satisfaction guaranteed</p>
  </section>
</body>
</html>
```